Business Card + Letterhead Design for KESTOVA TRADING INC.

We already have a logo; now we need a business card + letterhead. We import and distribute flags and souvenirs with an emphasis on soccer related memorabilia. We target various ethnic markets and sporting goods stores. "International Souvenirs"

```html
<!DOCTYPE html>
<html lang="en">
<head>
<meta charset="utf-8">
<title>Kestova Trading Inc. — Stationery</title>
<link rel="stylesheet" href="https://fonts.googleapis.com/css2?family=PT+Sans:wght@400;700&display=swap">
<style>
  :root {
    --backdrop: #d9d9d9;
    --paper: #ffffff;
    --ink: #111111;
    --ink-soft: #333333;
    --brand-red: #8a1a1f;
    --window: #e6e6e6;
    --muted: #cfcfcf;
    --font: "PT Sans", Arial, sans-serif;
  }
  * { box-sizing: border-box; margin: 0; padding: 0; }
  html, body { width: 1200px; height: 784px; overflow: hidden; }
  body { background: var(--backdrop); font-family: var(--font); color: var(--ink); }
  .canvas { position: relative; width: 1200px; height: 784px; }

  .sheet { position: absolute; background: var(--paper); overflow: hidden; box-shadow: 0 4px 14px rgba(0,0,0,.25); }
  .wave { position: absolute; left: 0; bottom: 0; width: 100%; display: block; }

  .brand { display: flex; flex-direction: column; }
  .brand-row { display: flex; align-items: center; gap: 8px; }
  .brand-dot { border-radius: 50%; background: var(--ink); flex: none; }
  .brand-name { color: var(--brand-red); font-weight: 700; letter-spacing: .04em; white-space: nowrap; line-height: 1; }
  .brand-tagline { color: var(--ink); white-space: nowrap; }

  .contact { display: grid; grid-template-columns: auto auto; column-gap: 6px; line-height: 1.3; color: var(--ink-soft); }
  .contact .web { grid-column: 1 / 3; }

  /* Letterhead */
  .letterhead { left: 40px; top: 60px; width: 440px; height: 570px; }
  .letterhead .brand { position: absolute; left: 24px; top: 34px; }
  .letterhead .brand-dot { width: 20px; height: 20px; }
  .letterhead .brand-name { font-size: 20px; }
  .letterhead .brand-tagline { font-size: 10px; margin: 3px 0 0 28px; }
  .letterhead .contact { position: absolute; left: 270px; top: 26px; font-size: 9.5px; }
  .letterhead .wave { height: 110px; }

  /* Business card front */
  .card-front { left: 520px; top: 60px; width: 300px; height: 172px; }
  .card-front .brand { position: absolute; left: 16px; top: 24px; }
  .card-front .brand-dot { width: 18px; height: 18px; }
  .card-front .brand-name { font-size: 17px; }
  .card-front .brand-tagline { font-size: 8.5px; margin: 3px 0 0 26px; }
  .card-front .wave { height: 96px; }
  .card-front .holder { position: absolute; left: 16px; bottom: 22px; color: var(--paper); font-weight: 700; font-size: 11px; }
  .card-front .contact { position: absolute; left: 158px; bottom: 14px; font-size: 8px; color: var(--paper); padding-left: 8px; border-left: 1px solid #777; }

  /* Business card back */
  .card-back { left: 848px; top: 60px; width: 300px; height: 172px; background: var(--ink); }
  .card-back .brand { position: absolute; left: 0; right: 0; top: 58px; align-items: center; }
  .card-back .brand-dot { width: 20px; height: 20px; background: var(--paper); }
  .card-back .brand-name { font-size: 19px; }
  .card-back .web { position: absolute; left: 0; right: 0; bottom: 30px; text-align: center; color: var(--paper); font-size: 10px; letter-spacing: .2em; }

  /* Envelope */
  .envelope { left: 520px; top: 290px; width: 628px; height: 340px; background: transparent; box-shadow: none; overflow: visible; }
  .envelope .body { position: absolute; inset: 0; background: var(--paper); border-radius: 2px; overflow: hidden; box-shadow: 0 4px 14px rgba(0,0,0,.25); }
  .envelope .flap { position: absolute; left: 0; top: 0; width: 100%; height: 110px; display: block; }
  .envelope .brand { position: absolute; left: 30px; top: 128px; }
  .envelope .brand-dot { width: 20px; height: 20px; }
  .envelope .brand-name { font-size: 20px; }
  .envelope .brand-tagline { font-size: 10px; margin: 3px 0 0 28px; }
  .envelope .address-window { position: absolute; left: 34px; top: 196px; width: 160px; height: 58px; border-radius: 8px; background: var(--window); border: 1px solid var(--muted); }
  .envelope .wave { height: 90px; }
</style>
</head>
<body>
<main class="canvas">

  <!-- Letterhead -->
  <section class="sheet letterhead" aria-label="Letterhead">
    <div class="brand">
      <div class="brand-row"><span class="brand-dot"></span><span class="brand-name">KESTOVA TRADING</span></div>
      <span class="brand-tagline">International Flags &amp; Souvenirs</span>
    </div>
    <div class="contact">
      <span>Phone</span><span>: (555) 201-3370</span>
      <span>Fax</span><span>: (555) 446-0192</span>
      <span>Email</span><span>: sales@kestovatrading.ca</span>
      <span class="web">www.kestovatrading.ca</span>
    </div>
    <svg class="wave" viewBox="0 0 440 110" preserveAspectRatio="none" aria-hidden="true">
      <path d="M0 80 C120 96 260 60 440 28 L440 110 L0 110 Z" fill="var(--ink)"/>
      <path d="M0 74 C120 90 260 54 440 20" fill="none" stroke="var(--brand-red)" stroke-width="3"/>
    </svg>
  </section>

  <!-- Business card, front -->
  <section class="sheet card-front" aria-label="Business card front">
    <div class="brand">
      <div class="brand-row"><span class="brand-dot"></span><span class="brand-name">KESTOVA TRADING</span></div>
      <span class="brand-tagline">International Flags &amp; Souvenirs</span>
    </div>
    <svg class="wave" viewBox="0 0 300 96" preserveAspectRatio="none" aria-hidden="true">
      <path d="M0 18 C80 40 180 34 300 4 L300 96 L0 96 Z" fill="var(--ink)"/>
      <path d="M0 12 C80 34 180 28 300 -2" fill="none" stroke="var(--brand-red)" stroke-width="2.5"/>
    </svg>
    <p class="holder">Daniel Verhoek</p>
    <div class="contact">
      <span>Phone</span><span>: (555) 201-3370</span>
      <span>Fax</span><span>: (555) 446-0192</span>
      <span>Email</span><span>: sales@kestovatrading.ca</span>
      <span class="web">www.kestovatrading.ca</span>
    </div>
  </section>

  <!-- Business card, back -->
  <section class="sheet card-back" aria-label="Business card back">
    <div class="brand">
      <div class="brand-row"><span class="brand-dot"></span><span class="brand-name">KESTOVA TRADING</span></div>
    </div>
    <p class="web">www.kestovatrading.ca</p>
  </section>

  <!-- Envelope -->
  <section class="sheet envelope" aria-label="Envelope">
    <div class="body">
      <svg class="flap" viewBox="0 0 628 110" preserveAspectRatio="none" aria-hidden="true">
        <path d="M0 0 L628 0 L628 66 C560 100 500 110 314 110 C128 110 68 100 0 66 Z" fill="var(--ink)"/>
      </svg>
      <div class="brand">
        <div class="brand-row"><span class="brand-dot"></span><span class="brand-name">KESTOVA TRADING</span></div>
        <span class="brand-tagline">International Flags &amp; Souvenirs</span>
      </div>
      <div class="address-window"></div>
      <svg class="wave" viewBox="0 0 628 90" preserveAspectRatio="none" aria-hidden="true">
        <path d="M0 58 C180 74 400 50 628 10 L628 90 L0 90 Z" fill="var(--ink)"/>
        <path d="M0 52 C180 68 400 44 628 4" fill="none" stroke="var(--brand-red)" stroke-width="3"/>
      </svg>
    </div>
  </section>

</main>
</body>
</html>
```